Keystone Draftworks - business cards
A set of business cards for a company
Dear designers,
I suggest that we minimize the quantity of red and grey filled areas on the cards.
I favour more the versions where there is more white space and just some colored accents.
In my opinion it looks more appropriate for our corporate customers.
Thanks for your understanding.
It might be a good idea to print a QR code on the back side of the card if it fits logically.
Not necessary but I'd like to see some ideas with and without it.

```html
<!DOCTYPE html>
<html lang="en">
<head>
<meta charset="utf-8">
<title>Keystone Draftworks — Stationery Set</title>
<link rel="stylesheet" href="https://fonts.googleapis.com/css2?family=Roboto+Condensed:wght@400;700&family=Roboto:wght@400;500&display=swap">
<style>
  :root {
    --red: #c0151b;
    --red-dark: #7d0b0f;
    --grey: #6f7478;
    --grey-dark: #4a4e52;
    --paper: #ffffff;
    --bg-top: #fafafa;
    --bg-bottom: #e6e6e6;
    --ink: #333638;
    --caption: #7a7a7a;
  }
  * { margin: 0; padding: 0; box-sizing: border-box; }
  html, body { width: 1200px; height: 437px; overflow: hidden; }
  body {
    background: linear-gradient(180deg, var(--bg-top), var(--bg-bottom));
    font-family: "Roboto", sans-serif;
    color: var(--ink);
    position: relative;
  }
  .brand {
    font-family: "Roboto Condensed", sans-serif;
    font-weight: 700;
    color: var(--red);
    text-transform: uppercase;
    display: flex;
    align-items: center;
    gap: 5px;
    line-height: 1;
    white-space: nowrap;
  }
  .brand .dot { width: 0.55em; height: 0.55em; border-radius: 50%; background: var(--red); flex: none; }
  .brand .words { display: flex; flex-direction: column; }
  .brand .line-two { font-size: 0.62em; letter-spacing: 0.12em; margin-top: 1px; }
  .caption {
    position: absolute;
    font-size: 7px;
    color: var(--caption);
    text-align: center;
  }

  /* Identity block */
  .identity { position: absolute; left: 19px; top: 112px; width: 172px; }
  .identity .brand { font-size: 22px; }
  .identity .tagline { font-size: 7px; color: var(--grey); margin-top: 6px; margin-left: 18px; }

  /* Business cards */
  .card {
    position: absolute; left: 24px; width: 168px; height: 82px;
    background: var(--paper);
    box-shadow: 0 2px 5px rgba(0,0,0,.25);
    overflow: hidden;
  }
  .card-front { top: 173px; }
  .card-front .accent {
    position: absolute; left: 0; top: 0; bottom: 0; width: 9px;
    background: linear-gradient(180deg, var(--red), var(--red-dark));
  }
  .card-front .brand { position: absolute; left: 16px; top: 10px; font-size: 13px; }
  .card-front .person { position: absolute; right: 10px; top: 36px; text-align: right; }
  .card-front .name { font-family: "Roboto Condensed", sans-serif; font-weight: 700; color: var(--red); font-size: 9px; }
  .card-front .role { font-size: 5.5px; color: var(--grey); margin-top: 2px; }
  .card-front .contact { position: absolute; left: 16px; bottom: 7px; font-size: 5px; color: var(--grey); line-height: 1.5; }

  .card-back { top: 302px; }
  .card-back .band {
    position: absolute; left: 0; right: 0; bottom: 0; height: 10px;
    background: linear-gradient(90deg, var(--red-dark), var(--red));
  }
  .card-back .brand { position: absolute; left: 0; right: 0; top: 22px; justify-content: center; font-size: 13px; }
  .card-back .web { position: absolute; left: 0; right: 0; top: 50px; text-align: center; font-size: 5.5px; color: var(--grey); }

  /* Letterheads */
  .letterhead {
    position: absolute; top: 24px; width: 280px; height: 366px;
    background: var(--paper);
    box-shadow: 0 2px 6px rgba(0,0,0,.25);
  }
  .letterhead-one { left: 211px; }
  .letterhead-two { left: 521px; }
  .letterhead .accent {
    position: absolute; left: 0; top: 0; bottom: 0; width: 12px;
    background: linear-gradient(180deg, var(--red), var(--red-dark));
  }
  .letterhead .brand { position: absolute; left: 24px; top: 16px; font-size: 16px; }
  .letterhead .contact {
    position: absolute; left: 170px; top: 14px; font-size: 5px; line-height: 1.6; color: var(--grey);
    border-left: 1px solid var(--red); padding-left: 5px;
  }
  .letterhead .footer {
    position: absolute; left: 12px; right: 0; bottom: 10px; text-align: center; font-size: 5px; color: var(--grey);
  }

  /* Envelopes */
  .envelopes { position: absolute; left: 818px; top: 24px; width: 310px; height: 366px; }
</style>
</head>
<body>

  <header class="identity">
    <div class="brand"><span class="dot"></span><span class="words"><span>Keystone</span><span class="line-two">Draftworks</span></span></div>
    <div class="tagline">Drafting Concepts</div>
  </header>

  <section class="card card-front">
    <div class="accent"></div>
    <div class="brand"><span class="dot"></span><span class="words"><span>Keystone</span><span class="line-two">Draftworks</span></span></div>
    <div class="person">
      <div class="name">Tobias</div>
      <div class="role">Senior Engineer</div>
    </div>
    <div class="contact">T +1 555 0142<br>hello@keystonedraft.com</div>
  </section>
  <p class="caption" style="left:24px; width:168px; top:280px;">Business Card Front</p>

  <section class="card card-back">
    <div class="brand"><span class="dot"></span><span class="words"><span>Keystone</span><span class="line-two">Draftworks</span></span></div>
    <div class="web">keystonedraft.com</div>
    <div class="band"></div>
  </section>
  <p class="caption" style="left:24px; width:168px; top:392px;">Business Card Back</p>

  <section class="letterhead letterhead-one">
    <div class="accent"></div>
    <div class="brand"><span class="dot"></span><span class="words"><span>Keystone</span><span class="line-two">Draftworks</span></span></div>
    <div class="contact">T +1 555 0142<br>F +1 555 0143<br>mail@keystonedraft.com<br>keystonedraft.com</div>
    <div class="footer">keystonedraft.com</div>
  </section>
  <p class="caption" style="left:211px; width:280px; top:398px;">Letterhead Page One</p>

  <section class="letterhead letterhead-two">
    <div class="accent"></div>
    <div class="brand"><span class="dot"></span><span class="words"><span>Keystone</span><span class="line-two">Draftworks</span></span></div>
    <div class="contact">T +1 555 0142<br>F +1 555 0143<br>mail@keystonedraft.com<br>keystonedraft.com</div>
    <div class="footer">14 Harbor Lane, Suite 3, Millbrook</div>
  </section>
  <p class="caption" style="left:521px; width:280px; top:398px;">Letterhead Page Two</p>

  <svg class="envelopes" viewBox="0 0 310 366" aria-hidden="true">
    <defs>
      <linearGradient id="flap-grey" x1="0" y1="0" x2="0" y2="1">
        <stop offset="0" stop-color="#7a7f83"/><stop offset="1" stop-color="#4a4e52"/>
      </linearGradient>
      <linearGradient id="flap-red" x1="0" y1="0" x2="0" y2="1">
        <stop offset="0" stop-color="#c0151b"/><stop offset="1" stop-color="#7d0b0f"/>
      </linearGradient>
      <filter id="env-shadow" x="-5%" y="-10%" width="110%" height="130%">
        <feDropShadow dx="0" dy="2" stdDeviation="2" flood-opacity=".25"/>
      </filter>
    </defs>
    <g filter="url(#env-shadow)">
      <rect x="5" y="0" width="300" height="100" fill="#fff"/>
      <path d="M5 0 H305 V35 L155 70 L5 35 Z" fill="url(#flap-grey)"/>
      <circle cx="155" cy="38" r="4" fill="#fff"/>
    </g>
    <g filter="url(#env-shadow)">
      <rect x="5" y="80" width="300" height="100" fill="#fff"/>
      <path d="M5 80 L155 125 L305 80 Z" fill="url(#flap-red)"/>
      <circle cx="155" cy="104" r="4" fill="#fff"/>
    </g>
    <g filter="url(#env-shadow)">
      <rect x="5" y="160" width="300" height="100" fill="#fff"/>
      <path d="M5 160 L155 200 L305 160" fill="none" stroke="#d8d8d8" stroke-width="1"/>
      <circle cx="155" cy="190" r="4" fill="#c0151b"/>
    </g>
    <g filter="url(#env-shadow)">
      <rect x="5" y="240" width="300" height="110" fill="#fff"/>
      <rect x="5" y="240" width="6" height="110" fill="#c0151b"/>
      <circle cx="24" cy="256" r="3" fill="#c0151b"/>
      <text x="31" y="259" font-family="Roboto Condensed, sans-serif" font-weight="700" font-size="8" fill="#c0151b">KEYSTONE DRAFTWORKS</text>
    </g>
  </svg>
  <p class="caption" style="left:818px; width:310px; top:398px;">Envelope Set</p>

</body>
</html>
```